Building Company Business Card Design

Need a design for a business card:
It needs to have: Name, Phone, Facebook link, Website, email
i would also like a list of works we undertake:
-New Homes
-Extensions, Renovations & Bathrooms
-Decking, Carports, Sheds (Residential and Industrial)
-Carpentry
-Fences, Patios & Pergolas

Name, Phone, Facebook link, Website, email + details of services provided listed in description

```html
<!DOCTYPE html>
<html lang="en">
<head>
<meta charset="UTF-8">
<title>Crestline Homes – Business Card</title>
<link rel="stylesheet" href="https://fonts.googleapis.com/css2?family=Raleway:wght@400;500;700&family=Arimo:wght@400&display=swap">
<style>
  :root {
    --bg: #3a2a20;
    --metal-light: #f4f5f5;
    --metal-mid: #d9dadb;
    --metal-dark: #c4c6c7;
    --ink: #1e1e1e;
    --ink-soft: #444547;
    --grey: #6e6f71;
    --green: #2db34a;
    --screw: #b9bbbd;
  }
  * { margin: 0; padding: 0; box-sizing: border-box; }
  html, body { width: 1199px; height: 1200px; overflow: hidden; }
  body { background: var(--bg); position: relative; font-family: "Raleway", sans-serif; }

  .card {
    position: absolute; left: 206px; width: 787px; height: 460px;
    overflow: hidden;
    background: repeating-linear-gradient(180deg, var(--metal-mid) 0 2px, var(--metal-dark) 2px 3px, var(--metal-mid) 3px 5px);
    box-shadow: 0 4px 14px rgba(0,0,0,.45);
  }
  .card--front { top: 120px; }
  .card--back { top: 619px; }
  .card__surface { position: absolute; inset: 0; width: 100%; height: 100%; }

  .screw {
    position: absolute; width: 20px; height: 20px; border-radius: 50%;
    background: radial-gradient(circle at 40% 35%, #fff 0 20%, var(--screw) 60%, #7d7f81 100%);
    border: 1px solid #8d8f91; transform: translate(-50%, -50%);
  }

  .brand { position: absolute; left: 86px; top: 128px; color: var(--ink); font-weight: 700; }
  .brand__name { font-size: 29px; letter-spacing: .5px; line-height: 1; text-transform: uppercase; }
  .brand__sub { font-size: 14.5px; letter-spacing: .3px; line-height: 1.3; text-transform: uppercase; }

  .person { position: absolute; left: 81px; top: 254px; color: var(--ink-soft); }
  .person__name { font-size: 27px; font-weight: 400; line-height: 1.05; }
  .person__role { font-size: 20px; font-weight: 400; line-height: 1.1; }

  .contacts { position: absolute; left: 81px; top: 325px; list-style: none; color: var(--ink-soft); }
  .contacts li { display: flex; align-items: center; height: 25.5px; font-size: 21px; }
  .contacts svg { width: 15px; height: 15px; margin-right: 10px; fill: var(--ink-soft); }

  .services { position: absolute; left: 345px; top: 66px; list-style: none; font-family: "Arimo", sans-serif; font-size: 16.5px; color: var(--ink); }
  .services li { position: relative; padding-left: 22px; line-height: 23px; margin-bottom: 3.5px; }
  .services li::before { content: ""; position: absolute; left: 5px; top: 8px; width: 8px; height: 8px; background: var(--green); }

  .mark { position: absolute; left: 503px; top: 290px; display: flex; align-items: center; gap: 10px; color: var(--green); font-weight: 700; font-size: 38px; letter-spacing: 1px; }
  .mark__square { width: 30px; height: 30px; background: var(--green); }
</style>
</head>
<body>

<section class="card card--front" aria-label="Business card front">
  <svg class="card__surface" viewBox="0 0 787 460" preserveAspectRatio="none" aria-hidden="true">
    <defs>
      <radialGradient id="frontGlow" cx="0.45" cy="0.55" r="0.7">
        <stop offset="0" stop-color="#ffffff"/>
        <stop offset="0.7" stop-color="#f1f2f2"/>
        <stop offset="1" stop-color="#dcdedf"/>
      </radialGradient>
    </defs>
    <path d="M0,0 H605 C705,40 725,165 655,262 C565,382 405,432 246,460 H0 Z" fill="#cfd1d2"/>
    <path d="M0,0 H596 C694,40 712,162 643,258 C553,377 395,428 232,460 H0 Z" fill="url(#frontGlow)"/>
  </svg>
  <span class="screw" style="left:45px;top:34px"></span>
  <span class="screw" style="left:280px;top:34px"></span>
  <span class="screw" style="left:507px;top:34px"></span>
  <span class="screw" style="left:744px;top:34px"></span>
  <span class="screw" style="left:45px;top:230px"></span>
  <span class="screw" style="left:744px;top:230px"></span>
  <span class="screw" style="left:45px;top:426px"></span>
  <span class="screw" style="left:280px;top:426px"></span>
  <span class="screw" style="left:507px;top:426px"></span>
  <span class="screw" style="left:744px;top:426px"></span>

  <div class="brand">
    <p class="brand__name">Crestline Homes</p>
    <p class="brand__sub">and Developments Pty Ltd</p>
  </div>

  <div class="person">
    <p class="person__name">Name Surname</p>
    <p class="person__role">Designation</p>
  </div>

  <ul class="contacts">
    <li><svg viewBox="0 0 16 16"><path d="M3.5 1 6 3.8 4.7 5.6c.9 2 2.6 3.8 4.7 4.7L11.2 9 14 11.5l-1.3 2.3C7 14 2 9 2.2 3.3Z"/></svg>000-000-000</li>
    <li><svg viewBox="0 0 16 16"><path d="M1 4h14v1L8 9.5 1 5Zm0 2.5 7 4.5 7-4.5V13H1Z"/></svg>info@webaddress.com</li>
    <li><svg viewBox="0 0 16 16"><path d="M8 1a7 7 0 1 0 0 14A7 7 0 0 0 8 1Zm-.6 1.6v2.6H5.2c.5-1.4 1.3-2.4 2.2-2.6Zm1.2 0c.9.2 1.7 1.2 2.2 2.6H8.6Zm-4 3.8h2.8v3H4.4a9 9 0 0 1 .2-3Zm4 0h2.8a9 9 0 0 1 0 3H8.6Zm-6 0h1.7a10 10 0 0 0 0 3H2.6a5.7 5.7 0 0 1 0-3Zm10.1 0h1.7a5.7 5.7 0 0 1 0 3h-1.7a10 10 0 0 0 0-3ZM5.2 10.6h2.2v2.8c-.9-.2-1.7-1.3-2.2-2.8Zm3.4 0h2.2c-.5 1.5-1.3 2.6-2.2 2.8Z"/></svg>www.webaddress.com</li>
  </ul>
</section>

<section class="card card--back" aria-label="Business card back">
  <svg class="card__surface" viewBox="0 0 787 460" preserveAspectRatio="none" aria-hidden="true">
    <defs>
      <radialGradient id="backGlow" cx="0.55" cy="0.45" r="0.75">
        <stop offset="0" stop-color="#ffffff"/>
        <stop offset="0.7" stop-color="#f1f2f2"/>
        <stop offset="1" stop-color="#dcdedf"/>
      </radialGradient>
    </defs>
    <path d="M180,0 H787 V460 H539 C400,420 200,360 120,250 C75,180 95,60 180,0 Z" fill="#cfd1d2"/>
    <path d="M190,0 H787 V460 H553 C412,418 215,357 133,250 C88,180 110,60 190,0 Z" fill="url(#backGlow)"/>
  </svg>
  <span class="screw" style="left:43px;top:35px"></span>
  <span class="screw" style="left:280px;top:35px"></span>
  <span class="screw" style="left:507px;top:35px"></span>
  <span class="screw" style="left:741px;top:35px"></span>
  <span class="screw" style="left:43px;top:231px"></span>
  <span class="screw" style="left:741px;top:231px"></span>
  <span class="screw" style="left:43px;top:427px"></span>
  <span class="screw" style="left:280px;top:427px"></span>
  <span class="screw" style="left:507px;top:427px"></span>
  <span class="screw" style="left:741px;top:427px"></span>

  <ul class="services">
    <li>New Homes</li>
    <li>Extensions, Renovations &amp; Bathrooms</li>
    <li>Decking, Carports, Sheds<br>(Residential and Industrial)</li>
    <li>Carpentry</li>
    <li>Fences, Patios &amp; Pergolas</li>
  </ul>

  <div class="mark">
    <span class="mark__square"></span>
    <span>CRESTLINE</span>
  </div>
</section>

</body>
</html>
```